Non-profit for Addiction Counselors Needs Flyer & PowerPoint Slide Template for Learning Collab

We need a flyer and PowerPoint Slide template design for a non-profit organization based in Washington, DC called "BREMOL, The Guild for Recovery Practitioners". We are partnering with an organization called Lunetra Ark to provide "The Carewell Practice Growth Roundtable" that helps organizations maximize current funding and service opportunities inherent in healthcare reform and identify and address barriers to growth. The designs should be co-branded for both BREMOL and Lunetra Ark, with BREMOL represented first.

BREMOL, the Guild for Recovery Practitioners, represents the professional interests of more than 75,000 addiction counselors, educators and other addiction-focused health care professionals in the United States, Canada and abroad. BREMOL’s members are addiction counselors, educators and other addiction-focused health care professionals, who specialize in addiction prevention, treatment, recovery support and education. An important part of the healthcare continuum, BREMOL members and its 44 state affiliates work to create healthier individuals, families and communities through prevention, intervention, quality treatment and recovery support.

The purpose of the flyer is to promote and recruit customers to join the Learning Collaborative.

We would like to see designs that use blue, the main color of our website (www.bremol-guild.example) and fit nicely with the colors of the Lunetra Ark logo (gray and blue).

The final design should communicate professionalism and there is a great benefit to the organization for buying this product/joining this Collaborative.

Target Market(s)

Our membership potentials are addiction counselors or administrators of addiction treatment centers, women and men, aged 30 to 65 who are all trained as therapists and care about people.

Industry/Entity Type

Non-Profit

Font styles to use
Sans Serif

Colors
3377b5
cedeec
eaf1f7
5c5c5c

Requirements
Must have
• Package must include two pieces: promotional flyer and PowerPoint slide deck template.

Flyer: The flyer must be one page, be easy to read and clear, yet bright and colorful, and must appear best on the computer screen or opened on a tablet - most views will be online, with a small portion printed for handing out at conferences. Must have graphics - if a group of people, must be culturally diverse.

PowerPoint: Need main title slide, transition slide and main content slide templates that are coordinated with the flyer design elements or vice versa

Everything must contain our two logos - three are attached to choose from.
Everything must be clean and modern/contemporary in tone.

I included a sample application that I created for this project that shows what we have done so far, and how we wish to use the "combo logo" on other pieces created for this project.

```html
<!DOCTYPE html>
<html lang="en">
<head>
<meta charset="utf-8">
<title>Roundtable Slide Templates</title>
<link href="https://fonts.googleapis.com/css2?family=Lato:ital,wght@0,400;0,700;0,900;1,700;1,900&display=swap" rel="stylesheet">
<style>
  :root {
    --brand-blue: #1a74b9;
    --partner-gray: #4a4a4a;
    --frame-gray: #5c5c5c;
    --paper: #ffffff;
    --ink-light: #ffffff;
  }
  * { box-sizing: border-box; margin: 0; padding: 0; }
  html, body { width: 1200px; height: 467px; overflow: hidden; background: var(--paper); }
  body { position: relative; font-family: "Lato", Arial, sans-serif; }

  .quote-slide {
    position: absolute; left: 8px; top: 8px; width: 589px; height: 454px;
    background: var(--brand-blue); color: var(--ink-light);
  }
  .quote-mark { position: absolute; width: 44px; height: 40px; fill: var(--ink-light); }
  .quote-mark--open { left: 49px; top: 143px; }
  .quote-mark--close { left: 504px; top: 261px; }
  .quote-body {
    position: absolute; left: 110px; top: 162px; width: 440px;
    font-size: 22px; font-weight: 900; font-style: italic; line-height: 23px;
    letter-spacing: -0.2px;
  }
  .quote-author {
    position: absolute; left: 110px; top: 249px;
    font-size: 20px; font-weight: 700; letter-spacing: 0.4px;
  }

  .content-slide {
    position: absolute; left: 606px; top: 8px; width: 591px; height: 451px;
    border: 1px solid var(--frame-gray); background: var(--paper);
  }
  .cobrand {
    position: absolute; left: 354px; top: 375px; height: 50px; display: flex;
    box-shadow: 2px 3px 5px rgba(0,0,0,0.35);
  }
  .cobrand__partner {
    width: 134px; background: var(--partner-gray); color: var(--ink-light);
    padding: 8px 8px 0 8px; text-align: center; border: 2px solid #ddd; border-right: none;
  }
  .cobrand__partner-name { font-size: 9px; font-weight: 700; letter-spacing: 1px; text-align: left; }
  .cobrand__partner-line { font-size: 4.5px; letter-spacing: 0.6px; margin-top: 3px; }
  .cobrand__host {
    width: 92px; background: var(--brand-blue); color: var(--ink-light);
    border: 2px solid #ddd; padding: 3px 2px 0; text-align: center; overflow: hidden;
  }
  .cobrand__host-name { font-size: 15px; font-weight: 900; line-height: 16px; }
  .cobrand__host-site { font-size: 6px; font-weight: 700; margin-top: 1px; line-height: 7px; }
  .cobrand__host-tag {
    font-size: 5px; font-weight: 700; margin-top: 3px; line-height: 5.5px;
    white-space: normal;
  }
</style>
</head>
<body>
  <section class="quote-slide">
    <svg class="quote-mark quote-mark--open" viewBox="0 0 44 40" aria-hidden="true">
      <path d="M4 40 L4 24 Q4 6 18 0 L20 5 Q12 10 12 20 L18 20 L18 40 Z"/>
      <path d="M26 40 L26 24 Q26 6 40 0 L42 5 Q34 10 34 20 L40 20 L40 40 Z"/>
    </svg>
    <p class="quote-body">Lorem ipsum dolor sit amet, consectetur adipiscing elit. Vivamus a diam et lorem sollicitudin lacinia.</p>
    <p class="quote-author">Proin egestas</p>
    <svg class="quote-mark quote-mark--close" viewBox="0 0 44 40" aria-hidden="true">
      <path d="M18 0 L18 16 Q18 34 4 40 L2 35 Q10 30 10 20 L4 20 L4 0 Z"/>
      <path d="M40 0 L40 16 Q40 34 26 40 L24 35 Q32 30 32 20 L26 20 L26 0 Z"/>
    </svg>
  </section>

  <section class="content-slide">
    <div class="cobrand">
      <div class="cobrand__partner">
        <p class="cobrand__partner-name">Lunetra Ark, LLC</p>
        <p class="cobrand__partner-line">HUMAN SERVICES TECHNICAL SOLUTIONS</p>
        <p class="cobrand__partner-line">www.lunetra-ark.example</p>
      </div>
      <div class="cobrand__host">
        <p class="cobrand__host-name">BREMOL</p>
        <p class="cobrand__host-site">BREMOL-GUILD.EXAMPLE</p>
        <p class="cobrand__host-tag">THE GUILD FOR RECOVERY PRACTITIONERS</p>
      </div>
    </div>
  </section>
</body>
</html>
```